Redesign Of Hotel Coupon/Voucher 8.5 x 11

I would like to redesign my voucher.

Please provide me a color flyer design but one that would be easy on printing costs...for example printing from home computer/printer.

I would like to see some color designs...maybe some black and white and also full graphics and even basic like the plum rook voucher I provided as a sample. The 2 night hotel stay is the voucher I need to redesign...

Target Market(s)

Consumers

Industry/Entity Type

Hotel

Requirements
Must have
• exact text in current designs---look official, credible and trust worthy
Nice to have
• I would like to redesign my voucher.
• Please provide me a color flyer design but one that would be easy on printing costs...for example printing from home computer/printer.
• I would like to see some color designs...maybe some black and white and also full graphics and even basic like the plum rook voucher I provided as a sample. The 2 night hotel stay is the voucher I need to redesign...
Should not have

```html
<!DOCTYPE html>
<html lang="en">
<head>
<meta charset="utf-8">
<title>2 Night Hotel Stay Certificate</title>
<link href="https://fonts.googleapis.com/css2?family=Cinzel:wght@700&family=Open+Sans:wght@400;600;700&display=swap" rel="stylesheet">
<style>
:root{
  --blue:#0d52a0;
  --blue-dark:#08468c;
  --ink:#2b2b2b;
  --muted:#555;
  --rule:#cfd3d8;
  --canvas:#ececec;
  --paper:#ffffff;
}
*{box-sizing:border-box;margin:0;padding:0}
html,body{width:1020px;height:1200px;overflow:hidden;background:var(--canvas)}
body{font-family:"Open Sans",Arial,sans-serif;color:var(--ink)}
.sheet{position:absolute;left:60px;top:6px;width:900px;height:1188px;background:var(--paper);overflow:hidden}
.sheet-rule{position:absolute;top:300px;bottom:0;width:1px;background:var(--rule)}
.sheet-rule.left{left:30px}.sheet-rule.right{right:30px}
.hero-photo{position:absolute;left:0;top:0;width:900px;height:300px;
  background:linear-gradient(100deg,#3a2a22 0%,#6b5140 22%,#8c7a62 40%,#5d5660 58%,#3c3340 72%,#9aa6b2 88%,#d7dde2 100%)}
.title-band{position:absolute;left:60px;top:250px;width:393px;height:50px;background:var(--blue);
  color:#fff;font-family:"Cinzel",Georgia,serif;font-weight:700;font-size:29px;letter-spacing:.5px;
  display:flex;align-items:center;justify-content:center}
.compliments{position:absolute;left:541px;top:5px;width:290px;height:252px}
.compliments svg{position:absolute;inset:0}
.compliments-head{position:absolute;left:0;top:20px;width:290px;height:62px;background:var(--blue);color:#fff;text-align:center;padding-top:6px}
.compliments-head .small{font-size:15px;font-weight:600;letter-spacing:.3px;display:block}
.compliments-head .large{font-size:21px;letter-spacing:.4px;display:block;line-height:26px}
.compliments-field{position:absolute;left:0;width:290px;text-align:center;font-size:15px;font-weight:600;color:#222}
.destinations{position:absolute;left:67px;top:330px;width:750px;font-size:12.4px;line-height:16px;color:#222}
.destinations strong{color:var(--blue);font-weight:600}
.terms-title{position:absolute;left:67px;top:466px;font-size:18px;font-weight:600;color:var(--blue)}
.terms{position:absolute;left:67px;top:496px;width:750px;font-size:10.2px;line-height:12.45px;color:var(--muted);text-align:justify}
.redeem{position:absolute;left:67px;top:816px;width:276px;height:362px;background:var(--blue);color:#fff;padding:6px}
.redeem-inner{border:1.5px dashed rgba(255,255,255,.85);height:100%;text-align:center;padding:12px 10px 0}
.redeem-intro{font-size:11.6px;line-height:15.5px}
.redeem-ways{margin:10px auto 8px;width:196px;border:1.5px solid #fff;font-size:13.5px;font-weight:700;letter-spacing:.3px;padding:2px 0}
.redeem-step{font-size:11.4px;line-height:15px}
.redeem-step b{font-weight:700}
.redeem-meta{margin-top:22px;font-size:13px;font-weight:700;line-height:18px}
.redeem-meta-rule{border-top:1.5px dashed rgba(255,255,255,.85);margin:14px -10px 0}
.order-form{position:absolute;left:359px;top:815px;width:455px;height:302px;border:1.5px solid var(--blue)}
.form-divider{position:absolute;left:233px;top:16px;height:44px;width:1px;background:#888}
.form-col{position:absolute;top:12px}
.form-col.billing{left:18px;width:190px}
.form-col.payment{left:248px;width:195px}
.form-heading{font-size:12.4px;font-weight:600;color:var(--blue);letter-spacing:.2px;margin-bottom:6px}
.form-heading.spaced{margin-top:12px}
.field{display:flex;font-size:11px;line-height:16.5px;color:#444}
.field .line{flex:1;border-bottom:1px solid #777;margin:0 0 4px 2px}
.pay-label{font-size:12.4px;color:#444;margin:-4px 0 10px}
.checks{display:grid;grid-template-columns:62px 1fr;row-gap:3px;font-size:11px;color:#444;margin-bottom:8px}
.check::before{content:"";display:inline-block;width:8px;height:8px;border:1px solid var(--blue);margin-right:6px;vertical-align:0}
.field.blue{color:var(--blue)}
.agree{font-size:11px;color:#444;margin-top:8px}
.field.sign{font-weight:700;color:#333;margin-top:6px}
.fine{font-size:7px;line-height:9.5px;color:#666;margin-top:8px}
</style>
</head>
<body>
<div class="sheet">
  <div class="hero-photo" role="img" aria-label="Photo of a modern hotel suite with sofa, lamp and city window"></div>
  <div class="sheet-rule left"></div><div class="sheet-rule right"></div>

  <div class="compliments">
    <svg width="290" height="252" viewBox="0 0 290 252"><path d="M0 0H290V195L145 250L0 195Z" fill="#fff"/><path d="M10 8H280V190L145 241L10 190Z" fill="none" stroke="#0d52a0" stroke-width="1.2"/></svg>
    <div class="compliments-head"><span class="small">THE CERTIFICATE</span><span class="large">IS COMPLIMENTS OF:</span></div>
    <div class="compliments-field" style="top:102px">NAME:</div>
    <div class="compliments-field" style="top:147px">CONTACT NO:</div>
    <div class="compliments-field" style="top:192px">E-MAIL ADDRESS:</div>
  </div>

  <div class="title-band">2 NIGHT HOTEL STAY</div>

  <p class="destinations"><strong>Destinations Available:</strong> Anaheim, CA--Atlanta, GA--Atlantic City, NJ--Branson, MO--Cancun, MX--Charleston, SC--Coeur d' Alene, ID--Daytona Beach,FL--Destin, FL--Ft. Lauderdale, FL--Ft. Meyers, FL--Gatlinburg, TN--Hilton Head, SC--Honolulu, HI--Kissimmee, FL--Lake Tahoe, CA--Las Vegas,NV--Myrtle Beach, SC--Niagara Falls/Buffalo Area, NY--Orlando, FL--Ormond Beach, FL--Palm Springs, CA--Pigeon Forge, TN--St. Petersburg, FL--San Antonio, TX--San Diego, CA--San Francisco, CA--Sedona, AZ--Sonoma Wine Country, CA--St. George, UT--Tampa, FL--Williamsburg, VA--Wisconsin Dells, WI--Tallahassee, FL--Augusta, GA--Columbia, SC--New York, NY--Florence, SC--Washington, D.C.--Chicago, IL--Salt Lake City, UT--Hollywood, CA-Dayton, OH--Tucson, AZ--Niagra Falls, ON/CAN--Seattle, WA--Portland, OR--Antioch, CA--San Mateo, CA--Brunswick, GA--Nashville, TN</p>

  <h2 class="terms-title">Terms &amp; Conditions</h2>
  <p class="terms">This certificate will be considered void if bartered or purchased for legal tender by the recipient. This certificate is valid for a reservation request form offering 2 adults 21 years of age and older plus up to 2 children under the age of 18, 2 nights of hotel accommodations in the city of their choice of available cities. The cost to activate this certificate to receive the reservation request form is just a one-time non-refundable $14.95 processing fee. The cost upon requesting reservations is just a tax &amp; fee deposit of $33 per night. Taxes &amp; fees usually range from $12-$33 per night depending on when and where you travel to. If the taxes &amp; fees are less than the $33 per night the difference will be refunded after travel is completed. 30 days advance reservation notice is required. In order to guarantee that you will show up to your booked reservation you will be required to pay a REFUNDABLE $50 “Reservation Guarantee Deposit”. If you send in your travel dates, etc and you do not end up traveling then the reservation guarantee deposit will not be refundable. 7 days before and after holidays and conventions are not available. This offer is valid 7 days a week subject to availability. Friday and Saturday nights will require a surcharge of $20 per night. A $5 per person per night surcharge is enforced for each child up to 2 children under the age of 18. This offer is not valid for group travel. The recipient of this certificate is responsible for all expenses including but not limited to: transfers, food, gratuities, all pertinent fees, taxes, hotel surcharges, resort fees and any other miscellaneous expenses. If you activate this certificate online you will be able to instantly print your reservation request form. If you cannot print your own reservation request form we will mail it to you. You should receive it in the mail within 14 days. This certificate cannot be combined with any other promotional vacation offer. The expiration date on this certificate pertains only to activation of this certificate and not actual travel. You must activate this certificate by the expiration date printed on this certificate in order to receive the reservation request form. You must fill out the reservation request form with your destination choices and arrival dates and mail it to our fulfillment department within 6 months after activation, however travel can be completed within 12 months after activation. You will be required to give the travel agency multiple arrival dates and destinations. Only one 2 Night Hotel certificate Per Household Per Year. This certificate has no cash surrender value, void if discontinued and where prohibited by law. The terms of this offer are subject to change without notice. Do not rely upon representations other than what is printed on this certificate or the reservation request form. CST # 4471308</p>

  <div class="redeem">
    <div class="redeem-inner">
      <p class="redeem-intro">Simply fill out the form on this certificate and enclose payment of U.S. $14.95. Veyra, Meridian Card, Amberline Express, Dovecard, Debit Card, Check Card, Check &amp; Money Orders are all accepted.</p>
      <div class="redeem-ways">3 WAYS TO REDEEM:</div>
      <p class="redeem-step"><b>1. For expedited redemption go to:</b><br>www.StayRewardsClub.com</p>
      <p class="redeem-step" style="margin-top:6px"><b>2. Fax* certificate to: 1-800-555-0142</b></p>
      <p class="redeem-step"><b>3. Mail* to:</b><br>Redemption Center<br>4260 Harbor View Rd Ste 210<br>Lakeport, Ca 95453</p>
      <div class="redeem-meta-rule"></div>
      <p class="redeem-meta">Certificate ID: -10002<br>Expiration Date: 04/08/2017</p>
    </div>
  </div>

  <div class="order-form">
    <div class="form-divider"></div>
    <div class="form-col billing">
      <h3 class="form-heading">BILLING INFORMATION</h3>
      <div class="field">Name:<span class="line"></span></div>
      <div class="field">Address:<span class="line"></span></div>
      <div class="field">City:<span class="line"></span></div>
      <div class="field">State:<span class="line"></span></div>
      <div class="field">Zip Code:<span class="line"></span></div>
      <div class="field">Country:<span class="line"></span></div>
      <div class="field">Phone:<span class="line"></span></div>
      <div class="field">Email:<span class="line"></span></div>
      <h3 class="form-heading spaced">SHIPPING INFORMATION</h3>
      <div class="field">Name:<span class="line"></span></div>
      <div class="field">Address:<span class="line"></span></div>
      <div class="field">City:<span class="line"></span></div>
      <div class="field">State:<span class="line"></span></div>
      <div class="field">Zip Code:<span class="line"></span></div>
      <div class="field">Country:<span class="line"></span></div>
    </div>
    <div class="form-col payment">
      <h3 class="form-heading">PAYMENT INFORMATION</h3>
      <p class="pay-label">Payment Method:</p>
      <div class="checks">
        <span class="check">Check</span><span class="check">Money Order</span>
        <span class="check">Veyra</span><span class="check">Meridian Card</span>
        <span class="check">AMBX</span><span class="check">Dovecard</span>
      </div>
      <div class="field blue">Name On Card:<span class="line"></span></div>
      <div class="field blue">Card # (16 digits):<span class="line"></span></div>
      <div class="field blue">Expiration Date:<span class="line"></span></div>
      <div class="field blue">CV2#**:<span class="line"></span></div>
      <p class="agree">I agree to terms and conditions</p>
      <div class="field sign">Signature:<span class="line"></span></div>
      <p class="fine">“Redemption Center” will appear on your billing statement. Make checks and money orders payable to: “Redemption Center”</p>
      <p class="fine" style="margin-top:5px">* You will receive your information by mail within 10 days.<br>** Last 3 digits on back of card (4 digits on front of AMBX).</p>
    </div>
  </div>
</div>
</body>
</html>
```